Brotar Nutrição Web Site design

Build a fluid / html5 web site for Brotar Nutrição a breastfeeding consultant small business.
For more info: https://www.facebook.com/brotarnutricao
Domain: www.brotarnutricao.com.br

Other breastfeeding consultant web sites:
http://nursingadvisorhub.ie/
http://www.qmvt.org/k7p/pages/index.cfm?pageid=1

Target Market(s)

New mothers, Mothers with Breastfeeding issues or questions

Industry/Entity Type

Business

Requirements
Must have
• Required "pages":
• - Services
• - Info
• - About Us
• - Contact (E-mail form, Map, address, phone information)
• - Scheduling: Calendar to pick a date, choose a service and that sends an e-mail to us: brotarnutricao@mailvexo.com. Customer receives a popup asking to wait for our contact. Possibility to block out dates by Admin.
Nice to have
• Use the color palette from the attached pictures
• Be fluid
Should not have
• No proprietary components (JS or other)
• No PHP

```html
<!DOCTYPE html>
<html lang="pt-BR">
<head>
<meta charset="utf-8">
<title>Brotar – Serviços de Apoio à Amamentação</title>
<link href="https://fonts.googleapis.com/css2?family=Open+Sans:wght@400;600;700;800&display=swap" rel="stylesheet">
<style>
:root{
  --red:#d9363e;
  --red-dark:#c22a31;
  --ink:#1a1a1a;
  --text:#555;
  --muted:#666;
  --brown:#5a4a3c;
  --purple:#6e68ac;
  --pink:#ec6f8c;
  --teal:#3fa7b3;
  --orange:#f7aa3b;
  --panel:#ebebeb;
  --footer:#ececec;
  --white:#fff;
}
*{margin:0;padding:0;box-sizing:border-box}
html,body{width:981px;height:1200px;overflow:hidden;background:var(--white)}
body{font-family:"Open Sans",Arial,sans-serif;color:var(--text);position:relative}
.page-shell{position:absolute;left:80px;top:20px;width:821px;height:600px;box-shadow:0 0 18px rgba(0,0,0,.07);border-radius:4px}
.abs{position:absolute}
.brand{left:94px;top:38px;display:flex;align-items:center;gap:8px;font-size:40px;font-weight:400;color:var(--brown);letter-spacing:.5px}
.brand-dot{width:10px;height:10px;border-radius:50%;background:var(--red);margin-top:-20px}
.contact-item{top:38px;display:flex;align-items:center;gap:8px;font-size:10.5px;color:#444}
.icon-circle{width:29px;height:29px;border-radius:50%;background:var(--red);display:flex;align-items:center;justify-content:center}
.main-nav a,.footer-nav a{color:#444;text-decoration:none}
.main-nav a{position:absolute;top:83px;font-size:10.5px}
.hero{left:94px;top:118px;width:792px;height:340px;border-radius:2px;background:linear-gradient(90deg,#e6b9c8 0%,#f0e4ea 35%,#efe2e4 55%,#e4c2b8 75%,#c98a7e 100%);overflow:hidden}
.hero-title{left:62px;top:74px;font-size:48px;font-weight:800;color:var(--ink);letter-spacing:-.5px}
.hero-sub{left:65px;top:128px;font-size:21px;color:#222}
.hero-text{left:66px;top:163px;width:320px;font-size:10.5px;line-height:20px;color:#333}
.btn{display:flex;align-items:center;justify-content:center;background:var(--red);color:var(--white);font-weight:700;text-transform:uppercase;border-radius:2px;box-shadow:0 2px 0 var(--red-dark)}
.hero-btn{left:67px;top:220px;width:120px;height:39px;font-size:12px}
.slider-arrows{left:738px;top:306px;display:flex;gap:2px}
.slider-arrows span{width:20px;height:20px;background:rgba(200,60,70,.35);display:flex;align-items:center;justify-content:center}
.card{top:472px;width:186px}
.card-photo{height:106px}
.card-label{height:33px;padding-left:16px;display:flex;align-items:center;color:var(--white);font-size:10px;font-weight:600;text-transform:uppercase}
.card-text{margin-top:12px;font-size:9.6px;line-height:18.3px;color:var(--muted)}
.cta{left:94px;top:727px;width:792px;height:79px;background:var(--panel);border:1px solid #dcdcdc;border-left:4px solid var(--teal)}
.cta-text{left:24px;top:21px;width:600px;font-size:9.4px;line-height:19px;color:#555}
.cta-btn{left:634px;top:21px;width:140px;height:37px;font-size:12px}
.video{left:94px;top:843px;width:337px;height:222px;background:linear-gradient(135deg,#f3ece8 0%,#eed5c6 45%,#e3b39c 70%,#f2e6df 100%)}
.play{left:137px;top:87px;width:64px;height:43px;border-radius:9px;background:var(--red);display:flex;align-items:center;justify-content:center}
.about-title{left:469px;top:841px;font-size:16px;font-weight:700;color:var(--red)}
.about-title small{font-size:11px;font-weight:400;color:#444;margin-left:3px}
.about-text{left:470px;width:404px;font-size:9.4px;line-height:18.3px;color:#555}
.read-btn{left:470px;top:1034px;width:106px;height:32px;font-size:10px}
.footer{left:0;top:1118px;width:981px;height:82px;background:var(--footer);border-top:1px solid #e0e0e0}
.footer-nav{left:94px;top:22px;font-size:9.6px;display:flex;gap:19px;color:#444}
.copy{left:94px;top:46px;font-size:9.6px;color:#444}
.social{left:593px;top:30px;display:flex;align-items:center;gap:5px;font-size:9.6px;color:#444}
.social-dot{width:22px;height:22px;border-radius:50%}
</style>
</head>
<body>
<div class="page-shell"></div>

<header>
  <div class="abs brand"><span>Brotar</span><span class="brand-dot"></span></div>

  <div class="abs contact-item" style="left:565px">
    <span class="icon-circle"><svg width="12" height="12" viewBox="0 0 24 24"><path fill="#fff" d="M6.6 10.8a15.1 15.1 0 0 0 6.6 6.6l2.2-2.2c.3-.3.7-.4 1-.2 1.1.4 2.3.6 3.6.6.6 0 1 .4 1 1V20c0 .6-.4 1-1 1A17 17 0 0 1 3 4c0-.6.4-1 1-1h3.5c.6 0 1 .4 1 1 0 1.3.2 2.5.6 3.6.1.3 0 .7-.2 1z"/></svg></span>
    <span>Call Us : ( 71 5550-2184 )</span>
  </div>
  <div class="abs contact-item" style="left:733px">
    <span class="icon-circle"><svg width="12" height="10" viewBox="0 0 24 18"><path fill="#fff" d="M0 2 12 10 24 2V0H0zM0 4.5V18h24V4.5L12 12.5z"/></svg></span>
    <span>Email Us : info@brotar.com.br</span>
  </div>

  <nav class="main-nav">
    <a style="left:458px">Home</a>
    <a style="left:528px">Services</a>
    <a style="left:609px">Info</a>
    <a style="left:670px">About us</a>
    <a style="left:754px">Contact</a>
    <a style="left:833px">Scheduling</a>
  </nav>
</header>

<section class="abs hero">
  <div role="img" aria-label="Photo of a mother kissing her smiling baby" class="abs" style="inset:0"></div>
  <h1 class="abs hero-title">Brotar</h1>
  <h2 class="abs hero-sub" style="font-weight:400">Serviços de Apoio à Amamentação</h2>
  <p class="abs hero-text">Lorem Ipsum is simply dummy text of the printing and typesetting industry. Lorem Ipsum has been the industry's standard</p>
  <a class="abs btn hero-btn">Click Here</a>
  <div class="abs slider-arrows">
    <span><svg width="6" height="9" viewBox="0 0 6 9"><path d="M5 1 1 4.5 5 8" stroke="#fff" fill="none"/></svg></span>
    <span><svg width="6" height="9" viewBox="0 0 6 9"><path d="M1 1 5 4.5 1 8" stroke="#fff" fill="none"/></svg></span>
  </div>
</section>

<section>
  <article class="abs card" style="left:94px">
    <div class="card-photo" role="img" aria-label="Photo of a mother cuddling her baby" style="background:linear-gradient(135deg,#e8cfc2,#d8a894 60%,#f1e4dc)"></div>
    <div class="card-label" style="background:var(--purple)">Lorem Ipsum is simply</div>
    <p class="card-text">Lorem Ipsum is simply dummy text of the printing and typesetting industry. Lorem Ipsum has been the industry's standard dummy text ever since...</p>
  </article>
  <article class="abs card" style="left:296px">
    <div class="card-photo" role="img" aria-label="Photo of hands forming a heart around baby feet" style="background:linear-gradient(135deg,#6b4a44,#c99483 50%,#7a5650)"></div>
    <div class="card-label" style="background:var(--pink)">Lorem Ipsum is simply</div>
    <p class="card-text">Lorem Ipsum is simply dummy text of the printing and typesetting industry. Lorem Ipsum has been the industry's standard dummy text ever since...</p>
  </article>
  <article class="abs card" style="left:498px">
    <div class="card-photo" role="img" aria-label="Photo of a pregnant woman resting on pillows" style="background:linear-gradient(135deg,#f4f4f4,#e2dcd8 55%,#f7f7f7)"></div>
    <div class="card-label" style="background:var(--teal)">Lorem Ipsum is simply</div>
    <p class="card-text">Lorem Ipsum is simply dummy text of the printing and typesetting industry. Lorem Ipsum has been the industry's standard dummy text ever since...</p>
  </article>
  <article class="abs card" style="left:700px">
    <div class="card-photo" role="img" aria-label="Photo of a smiling baby wrapped in a towel" style="background:linear-gradient(135deg,#d9d9d9,#f0d3c4 50%,#e9e9e9)"></div>
    <div class="card-label" style="background:var(--orange)">Lorem Ipsum is simply</div>
    <p class="card-text">Lorem Ipsum is simply dummy text of the printing and typesetting industry. Lorem Ipsum has been the industry's standard dummy text ever since...</p>
  </article>
</section>

<section class="abs cta">
  <p class="abs cta-text">Lorem Ipsum is simply dummy text of the printing and typesetting industry. Lorem Ipsum has been the industry's standard dummy text ever since the 1500s, when an unknown printer took a galley of type and scrambled</p>
  <a class="abs btn cta-btn">Get In Touch</a>
</section>

<section>
  <div class="abs video" role="img" aria-label="Video still of a sleeping newborn holding a parent's hand">
    <div class="abs play"><svg width="16" height="18" viewBox="0 0 16 18"><path d="M0 0 16 9 0 18z" fill="#fff"/></svg></div>
  </div>
  <h2 class="abs about-title">ABOUT BROTAR<small>SERVIÇOS DE APOIO À AMAMENTAÇÃO</small></h2>
  <p class="abs about-text" style="top:874px">Lorem Ipsum is simply dummy text of the printing and typesetting industry. Lorem Ipsum has been the industry's standard dummy text ever since the 1500s, when an unknown printer took a galley of type and scrambled it to make a type specimen book. It has survived not only five centuries, but also the leap into electronic typesetting.</p>
  <p class="abs about-text" style="top:965px">It has survived not only five centuries, but also the leap into electronic typesetting, remaining essentially unchanged. It was popularised in the 1960s with the release of Letraset sheets containing Lorem Ipsum passages, and more recently...</p>
  <a class="abs btn read-btn">Read More</a>
</section>

<footer class="abs footer">
  <nav class="abs footer-nav">
    <a>Home</a><span>/</span><a>Services</a><span>/</span><a>Info</a><span>/</span><a>About us</a><span>/</span><a>Contact</a><span>/</span><a>Scheduling</a>
  </nav>
  <p class="abs copy">© 2015. Brotar. All rights reserved.</p>
  <div class="abs social">
    <span style="margin-right:4px">Connect with our social network :</span>
    <span class="social-dot" style="background:#2f5a9e"></span>
    <span class="social-dot" style="background:#333"></span>
    <span class="social-dot" style="background:#1f6f8b"></span>
    <span class="social-dot" style="background:#d7262c"></span>
    <span class="social-dot" style="background:#3fa9dd"></span>
    <span class="social-dot" style="background:#d7262c"></span>
  </div>
</footer>
</body>
</html>
```